Tavor Management - Managing Urban Projects for the City of Modiin

Tavor Management needs a website that projects its professionalism and innovation to the residents of the city of Modiin. The design needs include: 1) a homepage design, 2) ~12 customized icons used on the homepage, 3) a layered image (city landscape with company logo on it) used as a fullwidth background image on the homepage. The client wants a site that is pleasant on the eye and easy to navigate. The client wants the site to project the organization as being professional and innovative.

Target Market(s)

adult residents of the city of modiin, israel

Industry/Entity Type

management of urban projects

Number of Pages Required

1 page

Font styles to use
Sans Serif

Requirements
Must have
• psd of design and psd of main fullwidth background image on the homepage
Nice to have
• icons for navigation bar and homepage teasers
Should not have
• colors should match the logo attached, font should be modern

```html
<!DOCTYPE html>
<html lang="he" dir="rtl">
<head>
<meta charset="utf-8">
<title>מנהלת תבור – מודיעין</title>
<link rel="stylesheet" href="https://fonts.googleapis.com/css2?family=Heebo:wght@300;400;500;700&display=swap">
<style>
:root{
  --green:#3f9a44;
  --green-dark:#2e7d32;
  --green-light:#63b95a;
  --tile:#3fae3f;
  --ink:#2b2b2b;
  --muted:#555;
  --grey-bg:#ececec;
  --white:#fff;
  --sky-top:#8fb3d6;
  --sky-bottom:#c9d6e0;
}
*{box-sizing:border-box;margin:0;padding:0}
html,body{width:1200px;height:2743px;overflow:hidden}
body{position:relative;font-family:'Heebo',sans-serif;color:var(--ink);background:var(--white)}
.abs{position:absolute}

/* sidebar */
.sidebar{position:absolute;right:0;top:0;width:115px;height:2743px;background:linear-gradient(180deg,#3d8e45 0%,#4a9e4d 50%,#5bb45a 100%);z-index:5}
.nav-item{height:75px;border-bottom:1px solid rgba(255,255,255,.18);display:flex;flex-direction:column;align-items:center;justify-content:center;color:var(--white);font-size:14px;font-weight:500;line-height:1.05;text-align:center;gap:4px}
.nav-item.home{background:rgba(0,0,0,.12);height:77px}
.nav-item svg{width:30px;height:30px;fill:none;stroke:#fff;stroke-width:1.6}

/* hero */
.hero{left:0;top:0;width:1085px;height:745px;background:linear-gradient(180deg,var(--sky-top) 0%,var(--sky-bottom) 38%,#8c9a80 46%,#6e7f55 70%,#4f6e3a 100%)}
.hero-brand{left:0;width:1085px;top:150px;text-align:center}
.hero-brand .mark{width:60px;height:60px;border-radius:50%;background:var(--green);margin:0 auto 14px}
.hero-brand .name{font-size:32px;font-weight:700;color:var(--green-dark)}
.hero-brand .tag{font-size:11px;color:#555;letter-spacing:3px;margin-top:2px}
.tiles{top:365px;left:155px;display:flex;gap:12px;direction:ltr}
.tile{width:202px;height:168px;background:rgba(56,170,56,.82);border:2px solid rgba(255,255,255,.85);border-radius:6px 50px 6px 50px;display:flex;flex-direction:column;align-items:center;justify-content:center;color:var(--white);font-size:21px;font-weight:500;gap:8px}
.tile.active{background:rgba(40,40,40,.72);border-radius:6px 50px 6px 50px}
.tile svg{width:52px;height:52px;fill:none;stroke:#fff;stroke-width:1.7}
.scroll-notch{left:508px;top:715px;width:90px;height:32px;background:var(--white);border-radius:45px 45px 0 0}
.scroll-notch svg{position:absolute;left:36px;top:8px}

/* about */
.about-dark{left:0;top:745px;width:300px;height:518px;background:linear-gradient(180deg,#3a3a3a,#6f6f6f)}
.about-back{left:80px;top:823px;width:258px;height:370px;background:var(--green-light)}
.about-photo{left:92px;top:836px;width:442px;height:344px;border-radius:70px 0 70px 0;background:linear-gradient(180deg,#8ea7b8 0%,#9aa79b 25%,#7f8c7c 55%,#6b7a5f 100%)}
.about-text{right:165px;top:855px;width:440px}
.eyebrow{color:var(--green);font-size:16px}
.heading{font-size:30px;font-weight:500;color:var(--ink);line-height:1.1}
.rule{width:56px;height:2px;background:var(--green);margin-top:10px}
.about-text p{font-size:12.5px;line-height:1.55;color:var(--muted);margin-top:22px}
.about-text p+p{margin-top:14px}

/* projects */
.projects{left:0;top:1263px;width:1085px;height:582px;background:linear-gradient(180deg,var(--grey-bg) 0%,#e2e2e2 60%,#cfd2cf 100%)}
.projects-head{left:0;width:1085px;top:1308px;text-align:center}
.projects-head .rule{margin:14px auto 0;width:62px}
.card{top:1424px;width:293px}
.card .photo{height:190px}
.card .body{position:relative;margin:-30px 20px 0;height:128px;background:var(--white);border-radius:0 0 50px 0;text-align:center;padding-top:22px;box-shadow:0 2px 6px rgba(0,0,0,.06)}
.card .body h3{font-size:20px;font-weight:400;color:#333}
.card .body small{display:block;font-size:8px;color:#777;margin-top:6px}
.card .body .btn{display:inline-block;margin-top:12px;width:104px;height:26px;line-height:26px;background:var(--green-dark);color:#fff;font-size:15px}
.card.featured .body{background:linear-gradient(135deg,#2e8b34,#4ab04a);color:#fff}
.card.featured .body h3,.card.featured .body small{color:#fff}
.card.featured .btn{background:transparent;border:1px solid #fff}
.arrow{top:1548px}

/* contact */
.contact{left:0;top:1845px;width:1085px;height:545px;background:linear-gradient(135deg,#2f8236 0%,#3f9a44 100%)}
.contact-text{left:92px;top:1940px;color:#fff;width:430px}
.contact-text .eyebrow{color:#fff}
.contact-text .heading{color:#fff;font-size:30px;font-weight:700}
.contact-text p{font-size:13px;margin-top:20px}
.field{background:#fff;color:#555;font-size:12px;padding:10px 16px;height:42px}
.btn-send{left:90px;top:2251px;width:150px;height:42px;border:2px solid #fff;color:#fff;font-size:18px;text-align:center;line-height:38px}
.ring{left:566px;top:1876px;width:466px;height:466px;border-radius:50%;border:2px solid rgba(255,255,255,.35)}
.ring2{left:580px;top:1890px;width:438px;height:438px;border-radius:50%;border:2px solid rgba(255,255,255,.6)}
.contact-photo{left:598px;top:1908px;width:402px;height:402px;border-radius:50%;background:linear-gradient(180deg,#a9c4dc 0%,#c5d2d6 22%,#7d9470 35%,#6fa048 60%,#4f8a34 100%)}
.contact-mark{left:790px;top:2292px;width:40px;height:40px;border-radius:50%;background:#fff}

/* footer */
.footer-col{top:2390px;height:285px;border-left:1px solid #ddd;padding-top:60px}
.footer-col h4{font-size:22px;font-weight:500;border-right:3px solid var(--green);padding-right:26px;line-height:1;margin-right:-3px}
.footer-col .inner{padding-right:29px;margin-top:16px;font-size:13px;line-height:1.6;color:#333}
.ic-row{display:flex;align-items:center;gap:10px;margin-bottom:18px}
.ic{width:28px;height:28px;border-radius:50%;background:var(--green);display:flex;align-items:center;justify-content:center}
.to-top{left:144px;top:2582px;width:32px;height:32px;border-radius:50%;background:#bbb}
.copy{left:0;top:2675px;width:1085px;height:68px;text-align:center;font-size:12px;color:#555;line-height:52px}
</style>
</head>
<body>

<nav class="sidebar">
  <div class="nav-item home"><svg viewBox="0 0 30 30"><path d="M5 14 15 5l10 9M8 12v12h5v-7h4v7h5V12"/></svg>בית</div>
  <div class="nav-item"><svg viewBox="0 0 30 30"><circle cx="15" cy="15" r="11"/><path d="M15 13v8M15 9v1"/></svg>אודות</div>
  <div class="nav-item"><svg viewBox="0 0 30 30"><path d="M6 12h5l11-6v18l-11-6H6zM9 18l2 7h3l-2-7"/></svg>מדיה וחדשות</div>
  <div class="nav-item"><svg viewBox="0 0 30 30"><circle cx="15" cy="15" r="5"/><path d="M15 4v4M15 22v4M4 15h4M22 15h4M7 7l3 3M20 20l3 3M23 7l-3 3M10 20l-3 3"/></svg>קידום פרויקטים</div>
  <div class="nav-item" style="height:88px"><svg viewBox="0 0 30 30"><path d="M5 26V10h8v16M13 26V5h12v21M8 14h2M8 18h2M16 9h2M20 9h2M16 13h2M20 13h2M16 17h2M20 17h2M3 26h24"/></svg>תכנון מוסדות<br>ציבור</div>
  <div class="nav-item" style="height:88px"><svg viewBox="0 0 30 30"><circle cx="15" cy="9" r="3"/><circle cx="9" cy="19" r="3"/><circle cx="21" cy="19" r="3"/><path d="M10 14h10M5 26c0-3 8-3 8 0M17 26c0-3 8-3 8 0"/></svg>מכרזים</div>
  <div class="nav-item"><svg viewBox="0 0 30 30"><rect x="6" y="5" width="18" height="20"/><path d="M9 9h12M9 13h6M9 17h12M9 21h12M17 12h4v3h-4z"/></svg>לוח מודעות</div>
  <div class="nav-item"><svg viewBox="0 0 30 30"><path d="M6 5h14v20H6zM9 9h8M9 13h8M9 17h4M17 22l8-9-2-2-8 9z"/></svg>פרויקטים</div>
  <div class="nav-item"><svg viewBox="0 0 30 30"><path d="M5 9h20v13H5zM5 9l10 7 10-7"/></svg>צור קשר</div>
</nav>

<!-- hero -->
<section class="abs hero" role="img" aria-label="Aerial view of Modiin with a park lake and city skyline"></section>
<div class="abs hero-brand">
  <div class="mark"></div>
  <div class="name">מנהלת תבור</div>
  <div class="tag">מודיעין | מכבים | רעות</div>
</div>
<div class="abs tiles">
  <div class="tile active"><svg viewBox="0 0 52 52"><path d="M8 10h26v34H8zM12 16h10M12 22h14M12 28h8M12 34h14M28 36l14-16-3-3-14 16z"/></svg>פרויקטים</div>
  <div class="tile"><svg viewBox="0 0 52 52"><circle cx="26" cy="12" r="6"/><circle cx="16" cy="32" r="6"/><circle cx="36" cy="32" r="6"/><path d="M18 22h16M8 46c0-5 16-5 16 0M28 46c0-5 16-5 16 0"/></svg>מכרזים</div>
  <div class="tile"><svg viewBox="0 0 52 52"><path d="M8 20h10l18-10v30L18 30H8zM12 30l4 12h5l-4-12M42 20v10"/></svg>קידום פרויקטים</div>
  <div class="tile"><svg viewBox="0 0 52 52"><rect x="10" y="6" width="30" height="38"/><path d="M15 12h20M15 18h10M28 17h7v6h-7zM15 24h10M15 30h20M15 36h20"/></svg>לוח מודעות</div>
</div>
<div class="abs scroll-notch"><svg width="18" height="30" viewBox="0 0 18 30" fill="none" stroke="#444" stroke-width="1.4"><rect x="3" y="1" width="12" height="18" rx="6"/><path d="M9 5v4M5 22l4 3 4-3M5 26l4 3 4-3"/></svg></div>

<!-- about -->
<div class="abs about-dark" role="img" aria-label="Monochrome city towers"></div>
<div class="abs about-back"></div>
<div class="abs about-photo" role="img" aria-label="Aerial view of a commercial centre with a parking lot"></div>
<div class="abs about-text">
  <div class="eyebrow">אודות</div>
  <div class="heading">אודות מנהלת תבור</div>
  <div class="rule"></div>
  <p>מנהלת תבור אחראית על ניהול פרויקטים עירוניים בעיר מודיעין, תכנון וביצוע של מבני ציבור, תשתיות ושטחים פתוחים לרווחת התושבים.</p>
  <p>המנהלת מקדמת פרויקטים חדשים בשיתוף העירייה, גופי התכנון והקבלנים, תוך הקפדה על איכות, שקיפות ועמידה בלוחות הזמנים – משלב התכנון ועד למסירה.</p>
  <p>לצד זאת פועלת המנהלת לשיפור השירות לתושבים, עדכון שוטף על התקדמות העבודות ומענה מהיר לפניות הציבור.</p>
  <p>אנו מזמינים אתכם להתעדכן בפרויקטים, במכרזים ובהודעות לציבור באתר זה.</p>
</div>

<!-- projects -->
<section class="abs projects"></section>
<div class="abs projects-head">
  <div class="eyebrow">פרויקטים</div>
  <div class="heading">פרויקטים שלנו</div>
  <div class="rule"></div>
</div>
<svg class="abs arrow" style="left:24px" width="22" height="40" viewBox="0 0 22 40" fill="none" stroke="#333" stroke-width="2"><path d="M20 2 2 20l18 18"/></svg>
<svg class="abs arrow" style="left:1040px" width="22" height="40" viewBox="0 0 22 40" fill="none" stroke="#333" stroke-width="2"><path d="M2 2l18 18L2 38"/></svg>

<div class="abs card" style="left:80px">
  <div class="photo" role="img" aria-label="Park lake with surrounding neighbourhoods" style="background:linear-gradient(180deg,#a8b9c9,#7a9466 55%,#4f7a45)"></div>
  <div class="body"><h3>פארק ענבה הרחבה</h3><small>תיאור קצר של הפרויקט, שלב הביצוע ומועד המסירה המתוכנן</small><span class="btn">עוד מידע</span></div>
</div>
<div class="abs card featured" style="left:395px">
  <div class="photo" role="img" aria-label="Entrance canopy of a public building" style="background:linear-gradient(180deg,#9fc1e0,#c9b35a 30%,#6d6a5c 60%,#3c4a3a)"></div>
  <div class="body"><h3>מרכז התרבות העירוני</h3><small>תיאור קצר של הפרויקט, שלב הביצוע ומועד המסירה המתוכנן</small><span class="btn">עוד מידע</span></div>
</div>
<div class="abs card" style="left:719px">
  <div class="photo" role="img" aria-label="Large industrial building with parking" style="background:linear-gradient(180deg,#9aa7b3,#bdbab0 45%,#7f8580)"></div>
  <div class="body"><h3>אזור התעשייה החדש</h3><small>תיאור קצר של הפרויקט, שלב הביצוע ומועד המסירה המתוכנן</small><span class="btn">עוד מידע</span></div>
</div>

<!-- contact -->
<section class="abs contact"></section>
<div class="abs contact-text">
  <div class="eyebrow">צור קשר</div>
  <div class="heading">השאירו לנו הודעה</div>
  <p>מלאו את הפרטים ונציג מטעמנו יחזור אליכם בהקדם.</p>
</div>
<div class="abs field" style="left:90px;top:2045px;width:212px">שם פרטי</div>
<div class="abs field" style="left:310px;top:2045px;width:214px">שם משפחה</div>
<div class="abs field" style="left:90px;top:2095px;width:212px">טלפון</div>
<div class="abs field" style="left:310px;top:2095px;width:214px">אימייל</div>
<div class="abs field" style="left:90px;top:2145px;width:434px;height:92px">הודעה</div>
<div class="abs btn-send">שלח</div>
<div class="abs ring"></div>
<div class="abs ring2"></div>
<div class="abs contact-photo" role="img" aria-label="Green park slope with trees and city buildings behind"></div>
<div class="abs contact-mark"></div>

<!-- footer -->
<div class="abs footer-col" style="left:730px;width:355px;border-left:none">
  <h4>קישורים</h4>
  <div class="inner" style="direction:ltr;text-align:right">קישור ראשון<br>PUBLIC WORKS<br>CITY PLANNING UPDATES<br>TENDERS AND NOTICES<br>תנאי שימוש</div>
</div>
<div class="abs footer-col" style="left:442px;width:288px">
  <h4>צור קשר</h4>
  <div class="inner">
    <div class="ic-row"><span class="ic"><svg width="14" height="14" viewBox="0 0 14 14" fill="#fff"><path d="M7 1a4 4 0 0 0-4 4c0 3 4 8 4 8s4-5 4-8a4 4 0 0 0-4-4zm0 5.5A1.5 1.5 0 1 1 7 3.5a1.5 1.5 0 0 1 0 3z"/></svg></span>מודיעין, שדרות הנחל 12</div>
    <div class="ic-row"><span class="ic"><svg width="14" height="14" viewBox="0 0 14 14" fill="#fff"><path d="M3 1l2 3-1 2c1 2 2 3 4 4l2-1 3 2-1 2C6 13 1 8 1 2z"/></svg></span>טלפון 08-9000123<br>פקס 08-9000124</div>
  </div>
</div>
<div class="abs footer-col" style="left:110px;width:332px">
  <h4>אודות</h4>
  <div class="inner">מנהלת תבור אחראית על ניהול פרויקטים עירוניים בעיר מודיעין, תכנון מבני ציבור, תשתיות ושטחים פתוחים לרווחת התושבים.</div>
</div>
<div class="abs to-top"><svg width="32" height="32" viewBox="0 0 32 32" fill="none" stroke="#fff" stroke-width="2"><path d="M11 18l5-5 5 5"/></svg></div>
<div class="abs copy">כל הזכויות שמורות © www.tavor-mgmt.example | נגישות | מודיעין - מנהלת תבור</div>

</body>
</html>
```